DL Flyer Design

I need a DL flyer, double-sided designed for a Brisbane based outdoor group exercise/training company called Step Up! Step Up! provides group outdoor training, designed for the individual. It provides the support, motivation and one-on-one attention of personal training combined with the support of a group environment. The classes are fun, challenging and aim to develop confidence & fitness. Weight loss is not the focus, although it is a benefit.
Updates

Hi

I've just uploaded a high res version of the logo if you need.

Cheers
Tam

Target Market(s)

English speaking men & women aged 25 - 45, white-collar office jobs. Average-low level of fitness, not hugely 'fitness' oriented but want to improve quality of life, overall fitness, lose a bit of weight.

Computer and consumer literate. Live in suburban Brisbane, Australia.

Industry/Entity Type

Training

Requirements
Must have
• Double sided DL. Use of black, greens and white per attached photos. Use of 1300 572 914 (1300 STEP UP) and website www.stepupactive.example.au

Indicative copy and contents is posted in the comments section.

```html
<!DOCTYPE html>
<html lang="en">
<head>
<meta charset="utf-8">
<title>Step Up! DL Flyer</title>
<link rel="stylesheet" href="https://fonts.googleapis.com/css2?family=Source+Sans+3:wght@400;600;700;900&display=swap">
<style>
  :root {
    --stage: #000000;
    --paper: #ffffff;
    --ink: #111111;
    --green: #5cb82e;
    --green-dark: #3f9a1c;
    --green-light: #8fd14f;
    --green-pale: #cfe9b8;
    --green-faint: #eef7e6;
    --photo-skin: #d9a98a;
    --photo-top: #e8d24a;
  }
  * { box-sizing: border-box; margin: 0; padding: 0; }
  html, body { width: 1200px; height: 900px; overflow: hidden; }
  body {
    background: var(--stage);
    font-family: "Source Sans 3", Arial, sans-serif;
    color: var(--ink);
    position: relative;
  }
  .flyer {
    position: absolute;
    top: 16px;
    width: 436px;
    height: 868px;
    background: var(--paper);
    overflow: hidden;
  }
  .flyer--front { left: 160px; }
  .flyer--back { left: 608px; }
  .abs { position: absolute; }

  .backdrop-figure {
    position: absolute;
    background: radial-gradient(ellipse at center, var(--green-faint) 0%, rgba(238,247,230,0) 70%);
  }

  .brand {
    position: absolute;
    font-weight: 900;
    color: var(--green);
    line-height: 1;
    display: flex;
    align-items: center;
    letter-spacing: -1px;
  }
  .brand__dot { border-radius: 50%; background: var(--green); flex: none; }
  .flyer--front .brand { top: 56px; left: 0; width: 436px; justify-content: center; font-size: 86px; gap: 12px; }
  .flyer--front .brand__dot { width: 24px; height: 24px; }
  .flyer--back .brand { top: 40px; left: 26px; font-size: 50px; gap: 8px; }
  .flyer--back .brand__dot { width: 14px; height: 14px; }

  .tagline { top: 218px; left: 0; width: 436px; text-align: center; font-weight: 700; font-size: 26px; line-height: 33px; }
  .headline { top: 306px; left: 0; width: 436px; text-align: center; font-weight: 900; font-size: 34px; line-height: 40px; color: var(--green); }
  .body-copy { left: 44px; width: 366px; font-size: 16px; line-height: 23px; }
  .body-copy strong { color: var(--green); font-weight: 700; }
  .copy-intro { top: 362px; }
  .copy-value { top: 444px; }
  .copy-trial { top: 500px; }
  .copy-note { top: 540px; color: var(--green); font-size: 15px; }
  .callout { top: 572px; left: 44px; font-weight: 900; font-size: 33px; line-height: 35px; }
  .callout span { color: var(--green); }
  .front-contact { top: 700px; left: 40px; }
  .front-contact .call-label { font-weight: 900; font-size: 17px; line-height: 20px; }
  .front-contact .phone { font-weight: 900; font-size: 26px; line-height: 27px; color: var(--green); }

  .photo { position: absolute; border-radius: 90px 90px 0 0; }
  .photo--front {
    left: 292px; top: 566px; width: 144px; height: 302px;
    background: linear-gradient(180deg, var(--photo-skin) 0%, var(--photo-top) 45%, #3a3a3a 100%);
  }
  .photo--back {
    left: 214px; top: 530px; width: 190px; height: 338px;
    background: linear-gradient(180deg, #e8c9a8 0%, var(--photo-skin) 40%, #5a3a6e 80%, #222 100%);
  }

  .wave { position: absolute; left: 0; bottom: 0; width: 436px; height: 90px; }
  .front-web { bottom: 14px; left: 0; width: 436px; text-align: center; color: var(--paper); font-size: 15px; font-weight: 600; }

  .program-title { top: 156px; left: 26px; font-weight: 900; font-size: 18px; }
  .schedule {
    position: absolute; top: 180px; left: 26px; width: 388px;
    border-collapse: collapse; font-size: 10px; table-layout: fixed;
  }
  .schedule th, .schedule td { border: 2px solid var(--paper); text-align: center; padding: 2px; }
  .schedule th { background: var(--green); color: var(--ink); font-weight: 700; height: 20px; }
  .schedule td { background: var(--green-pale); height: 38px; line-height: 12px; }
  .schedule td.time { font-weight: 700; }

  .back-call { top: 340px; left: 26px; font-weight: 900; font-size: 34px; line-height: 40px; }
  .back-phone { top: 384px; left: 26px; font-weight: 900; font-size: 44px; line-height: 50px; color: var(--green); }
  .back-web { top: 490px; left: 26px; font-weight: 900; font-size: 21px; }
  .back-location { top: 522px; left: 26px; font-size: 11px; }
</style>
</head>
<body>

<section class="flyer flyer--front">
  <div class="backdrop-figure" style="left:40px;top:560px;width:300px;height:240px" role="img" aria-label="Faint pale green running figure decoration"></div>
  <div class="photo photo--front" role="img" aria-label="Photo of a smiling woman in a yellow fitness top, hands on hips"></div>

  <div class="brand"><span class="brand__dot"></span>Step Up!</div>
  <p class="abs tagline">It's time to Step Up!<br>with group outdoor training</p>
  <h1 class="abs headline">Designed Just For You!</h1>

  <p class="abs body-copy copy-intro"><strong>Step Up!</strong> provides the unique combination of the one-on-one attention of personal training with the motivation and support of a group environment.</p>
  <p class="abs body-copy copy-value">Best of all, it's designed to fit fitness into your life - at an affordable price.</p>
  <p class="abs body-copy copy-trial">Curious? Give it a shot with a 1 week free trial!</p>
  <p class="abs body-copy copy-note">(Guaranteed no hard sell at the end)</p>

  <p class="abs callout">Tired of<br>hanging about?<br>.....Just <span>Step Up!</span></p>

  <div class="abs front-contact">
    <p class="call-label">Call Now :</p>
    <p class="phone">1300 572 914</p>
    <p class="phone">(1300 STEP UP)</p>
  </div>

  <svg class="wave" viewBox="0 0 436 90" preserveAspectRatio="none" aria-hidden="true">
    <path d="M0 28 Q218 -8 436 36 L436 90 L0 90 Z" fill="var(--green-light)"/>
    <path d="M0 46 Q218 18 436 54 L436 90 L0 90 Z" fill="var(--green)"/>
  </svg>
  <p class="abs front-web">www.stepupactive.example.au</p>
</section>

<section class="flyer flyer--back">
  <div class="backdrop-figure" style="left:60px;top:360px;width:360px;height:400px" role="img" aria-label="Faint pale green athletic figure decoration"></div>

  <div class="brand"><span class="brand__dot"></span>Step Up!</div>

  <h2 class="abs program-title">Session Program:</h2>
  <table class="schedule">
    <thead>
      <tr><th>Time</th><th>Monday</th><th>Tuesday</th><th>Wednesday</th><th>Thursday</th><th>Friday</th><th>Saturday</th></tr>
    </thead>
    <tbody>
      <tr><td class="time">6:00 am</td><td>Cardio</td><td></td><td>Boxing circuit</td><td>Cardio</td><td>Boxing circuit</td><td>Walk run</td></tr>
      <tr><td></td><td></td><td></td><td></td><td></td><td></td><td>One-on-One Sessions</td></tr>
      <tr><td class="time">6:00 pm</td><td>Strength</td><td>Cardio</td><td>Strength</td><td>Boxing circuit</td><td></td><td></td></tr>
    </tbody>
  </table>

  <p class="abs back-call">Call Now :</p>
  <p class="abs back-phone">1300 572 914<br>(1300 STEP UP)</p>
  <p class="abs back-web">www.stepupactive.example.au</p>
  <p class="abs back-location">Location: (**details not confirmed)</p>

  <svg class="wave" viewBox="0 0 436 90" preserveAspectRatio="none" aria-hidden="true">
    <path d="M0 18 Q200 -4 436 40 L436 90 L0 90 Z" fill="var(--green-light)"/>
    <path d="M0 40 Q218 14 436 58 L436 90 L0 90 Z" fill="var(--green)"/>
  </svg>
  <div class="photo photo--back" role="img" aria-label="Photo of a fit woman in a purple sports top wearing boxing gloves"></div>
</section>

</body>
</html>
```